Blue Heron IT Business Card - Clean, Simple

Need a simple, clean standard sized business card for an IT consulting business using existing logo and company colours. Background should be mainly white. Feel free to be creative but clean, simple, quiet design is preferred. Font is specified in logo but any sans serif fonts work.

Contact Information for card is as follows (doesn't need to be in this exact order):

Martin Calloway
Owner
martin@blueheronit.ca
705-391-2586
www.blueheronit.ca

Target Market(s)

Small to medium sized business.

Industry/Entity Type

IT Consulting

Contact Information for Business Card

Logo and contact info.

Font styles to use
Sans Serif

Colors
EE7325
F08F49
F5BC92
FAE3D3
FDF4ED

Requirements
Must have
• All white or mostly white background.

```html
<!DOCTYPE html>
<html lang="en">
<head>
<meta charset="utf-8">
<title>Blue Heron IT Business Card</title>
<link rel="stylesheet" href="https://fonts.googleapis.com/css2?family=Montserrat:wght@400;500;700&display=swap">
<style>
  :root {
    --orange: #ee7325;
    --orange-soft: #f08f49;
    --ink: #2b2b2d;
    --white: #ffffff;
    --stage: #2d2d2d;
  }
  * { margin: 0; padding: 0; box-sizing: border-box; }
  html, body { width: 1200px; height: 1015px; overflow: hidden; }
  body {
    background: var(--stage);
    font-family: "Montserrat", sans-serif;
    position: relative;
  }
  .card {
    position: absolute;
    left: 290px;
    width: 620px;
    height: 354px;
    overflow: hidden;
  }
  .card-front { top: 115px; background: var(--orange); }
  .card-back { top: 546px; background: var(--white); }
  .card-shape { position: absolute; inset: 0; width: 620px; height: 354px; }

  .brand {
    position: absolute;
    left: 0; right: 0;
    display: flex;
    align-items: center;
    justify-content: center;
    gap: 16px;
  }
  .brand-mark { width: 34px; height: 34px; border-radius: 50%; }
  .brand-name { font-weight: 700; font-size: 44px; letter-spacing: 0.5px; line-height: 1; }

  .card-front .brand { top: 104px; }
  .card-front .brand-mark { background: var(--white); }
  .card-front .brand-name { color: var(--white); }
  .front-web {
    position: absolute;
    left: 385px; top: 272px;
    font-size: 14px;
    letter-spacing: 2px;
    line-height: 1;
    color: var(--ink);
    white-space: nowrap;
    transform: rotate(-11deg);
    transform-origin: left center;
  }
  .front-web .domain { color: var(--orange); }

  .card-back .brand { top: 84px; }
  .card-back .brand-mark { background: var(--orange); }
  .card-back .brand-name { color: var(--ink); }

  .holder {
    position: absolute;
    left: 40px; top: 272px;
    width: 270px;
    color: var(--white);
    text-align: right;
  }
  .holder-name { font-weight: 700; font-size: 21px; letter-spacing: 0.5px; }
  .holder-role { font-weight: 500; font-size: 15px; margin-top: 2px; }
  .divider {
    position: absolute;
    left: 332px; top: 238px;
    width: 1.5px; height: 86px;
    background: var(--white);
  }
  .contacts {
    position: absolute;
    left: 350px; top: 236px;
    list-style: none;
    color: var(--white);
    font-size: 14px;
    font-weight: 500;
  }
  .contacts li { display: flex; align-items: center; gap: 9px; height: 29px; }
  .contacts svg { width: 15px; height: 15px; flex: none; }
</style>
</head>
<body>
  <section class="card card-front">
    <svg class="card-shape" viewBox="0 0 620 354" aria-hidden="true">
      <path d="M20 354 Q 300 250 620 200" fill="none" stroke="#ffffff" stroke-width="3"/>
      <path d="M45 354 Q 320 262 620 222 L620 354 Z" fill="#ffffff"/>
      <path d="M90 354 Q 380 300 620 270" fill="none" stroke="#ee7325" stroke-width="2.5"/>
    </svg>
    <div class="brand">
      <span class="brand-mark"></span>
      <span class="brand-name">Blue Heron IT</span>
    </div>
    <p class="front-web">www.<span class="domain">blueheronit</span>.ca</p>
  </section>

  <section class="card card-back">
    <svg class="card-shape" viewBox="0 0 620 354" aria-hidden="true">
      <path d="M0 300 Q 300 190 620 120" fill="none" stroke="#ee7325" stroke-width="3"/>
      <path d="M0 316 Q 310 208 620 138 L620 354 L0 354 Z" fill="#ee7325"/>
    </svg>
    <div class="brand">
      <span class="brand-mark"></span>
      <span class="brand-name">Blue Heron IT</span>
    </div>
    <div class="holder">
      <p class="holder-name">Martin Calloway</p>
      <p class="holder-role">Owner</p>
    </div>
    <span class="divider"></span>
    <ul class="contacts">
      <li>
        <svg viewBox="0 0 24 24" fill="none" stroke="#fff" stroke-width="2.2" stroke-linecap="round" stroke-linejoin="round"><path d="M22 16.9v3a2 2 0 0 1-2.2 2 19.8 19.8 0 0 1-8.6-3.1 19.5 19.5 0 0 1-6-6A19.8 19.8 0 0 1 2.1 4.2 2 2 0 0 1 4.1 2h3a2 2 0 0 1 2 1.7c.1.9.4 1.8.7 2.7a2 2 0 0 1-.5 2.1L8 9.8a16 16 0 0 0 6 6l1.3-1.3a2 2 0 0 1 2.1-.4c.9.3 1.8.6 2.7.7a2 2 0 0 1 1.7 2z"/></svg>
        705-391-2586
      </li>
      <li>
        <svg viewBox="0 0 24 24" fill="none" stroke="#fff" stroke-width="2.2" stroke-linejoin="round"><rect x="2" y="5" width="20" height="14" rx="1"/><path d="M2 6l10 7 10-7"/></svg>
        martin@blueheronit.ca
      </li>
      <li>
        <svg viewBox="0 0 24 24" fill="none" stroke="#fff" stroke-width="2"><circle cx="12" cy="12" r="10"/><path d="M2 12h20M12 2c3 3 4 6.5 4 10s-1 7-4 10c-3-3-4-6.5-4-10s1-7 4-10z"/></svg>
        www.blueheronit.ca
      </li>
    </ul>
  </section>
</body>
</html>
```